Business Card and Letterhead for Nurlo - modern real estate business

I need a double sided business card design for Nurlo. Please see business card brief here https://papers.trelvimo.net/sheet/q/7XrTbaLeZpMmQ2uWvd9HkCj4yNoEfsGi3lRtAz_pk/view?mode=shared

Please feel free to design the business cards however you feel best. I am happy to give some creative freedoms and then provide feedback from there.

Please then also create a letterhead to match the business card design

Colors

Designer to choose colors to be used in the design.

Requirements
Must have
• Must be a modern, elegant business card which looks very professional

```html
<!DOCTYPE html>
<html lang="en">
<head>
<meta charset="utf-8">
<title>Nurlo Letterhead</title>
<link rel="stylesheet" href="https://fonts.googleapis.com/css2?family=Montserrat:wght@400;700&family=Open+Sans:wght@400&display=swap">
<style>
  :root {
    --backdrop: #a6b7bd;
    --paper: #ffffff;
    --brand-red: #d7141e;
    --body-ink: #4a4a4a;
    --footer-ink: #222222;
    --rule: #6d6d6d;
    --signature-tone: #d9d9d9;
  }
  * { margin: 0; padding: 0; box-sizing: border-box; }
  html, body {
    width: 1200px; height: 907px; overflow: hidden;
    background: var(--backdrop);
  }
  .letterhead {
    position: absolute; left: 280px; top: 44px;
    width: 640px; height: 818px;
    background: var(--paper);
    font-family: "Open Sans", Arial, sans-serif;
    color: var(--body-ink);
  }
  .brand-name {
    position: absolute; top: 14px; left: 0; width: 100%;
    text-align: center;
    font-family: "Montserrat", Arial, sans-serif;
    font-weight: 700; font-size: 34px; letter-spacing: 1px;
    color: var(--brand-red);
  }
  .letter-date {
    position: absolute; left: 69px; top: 226px;
    font-size: 10.5px;
  }
  .letter-body {
    position: absolute; left: 69px; top: 268px;
    font-size: 10.5px; line-height: 24px;
    white-space: nowrap;
  }
  .letter-body p { margin-bottom: 1px; }
  .letter-body p + p { margin-top: 0; }
  .letter-body span { display: block; }
  .signature {
    position: absolute; left: 440px; top: 578px;
    width: 130px; height: 40px;
    background: linear-gradient(90deg, var(--signature-tone), #efefef);
    border-radius: 3px;
  }
  .signatory {
    position: absolute; left: 446px; top: 612px;
    font-size: 10.5px; line-height: 13px;
  }
  .footer-rule {
    position: absolute; left: 49px; top: 770px;
    width: 542px; height: 1px; background: var(--rule);
  }
  .footer-icons {
    position: absolute; left: 298px; top: 763px;
  }
  .footer-contacts {
    position: absolute; left: 0; top: 779px; width: 100%;
    text-align: center;
    font-family: "Montserrat", Arial, sans-serif;
    font-size: 10.5px; line-height: 16px;
    color: var(--footer-ink);
  }
  .footer-contacts .contact-line span { margin: 0 6px; }
</style>
</head>
<body>
  <main class="letterhead">
    <div class="brand-name">Nurlo</div>

    <div class="letter-date">Date, 10 September, 2020</div>

    <div class="letter-body">
      <p>
        <span>This is a sample letter that has been placed to demonstrate typing remat (Your Company). letterhead</span>
        <span>design. When positioned properly, it will serve to work in harmony with all other elements letterhead.</span>
        <span>This letterhead design is meant to project an image</span>
      </p>
      <p>
        <span>This letterhead design is meant project an image of professionalism reliability. By using simple aligen</span>
        <span>we have created a very spacious feeling. The simplicity suggest&nbsp; rengththe spaciousnes contributes h</span>
        <span>aesthetics the layout. These basic qualities along with the (Your Company)</span>
      </p>
      <p>
        <span>look and helps reinforce the (Your Company) brand. letterhead design is meant to project an image p</span>
        <span>design. When positioned properly, it will serve to work in harmony all the other elements letterhead.</span>
        <span>sionalism and reliability.</span>
      </p>
      <p>
        <span>This letterhead design is based on the (Form of your logo) form (Your Company) logo. Each stationery</span>
        <span>we have created a very spacious feeling. The simplicity suggests strength the spaciousnes contribute</span>
        <span>part of the (Form of your logo).</span>
      </p>
    </div>

    <div class="signature" role="img" aria-label="Handwritten signature of Daniel Harrow"></div>
    <div class="signatory">Daniel Harrow<br>Manager</div>

    <div class="footer-rule"></div>
    <svg class="footer-icons" width="44" height="14" viewBox="0 0 44 14" aria-hidden="true">
      <circle cx="7" cy="7" r="6" fill="#d7141e"/>
      <path d="M4.6 4.2c.4-.4.9-.4 1.2 0l.7.9c.2.3.2.6 0 .9l-.4.4c.4.8 1 1.4 1.8 1.8l.4-.4c.3-.2.6-.2.9 0l.9.7c.4.3.4.8 0 1.2l-.5.5C8.6 11 5.2 8.9 4.1 5.2z" fill="#fff"/>
      <circle cx="22" cy="7" r="6" fill="#d7141e"/>
      <rect x="18.6" y="4.6" width="6.8" height="4.8" rx=".5" fill="#fff"/>
      <path d="M18.8 4.9 22 7.3l3.2-2.4" fill="none" stroke="#d7141e" stroke-width=".7"/>
      <circle cx="37" cy="7" r="6" fill="#d7141e"/>
      <circle cx="37" cy="7" r="3.4" fill="none" stroke="#fff" stroke-width=".9"/>
      <path d="M33.6 7h6.8M37 3.6c-1.4 1.8-1.4 5 0 6.8M37 3.6c1.4 1.8 1.4 5 0 6.8" fill="none" stroke="#fff" stroke-width=".7"/>
    </svg>
    <div class="footer-contacts">
      <div class="contact-line"><span>0400 318 572</span><span>mara@nurlo.com</span><span>www.nurlo.com</span></div>
      <div>PO Box 1186, Calderwood NSW 2640</div>
    </div>
  </main>
</body>
</html>
```